Vitamin B12 Liquid Drops Label

hi, i need a label designed for my vitamin b12 drops that i am going to be selling on bazaroo. the label needs to quickly capture the attention of a buyer as he or she is scrolling through the thumbnail search results on bazaroo.example my brand is called zulpa. i already have an example brand logo i will be using, however, i need help designing the rest of the label. attached are some examples of labels i like for other supplements.some of these examples are pink. i do not want pink. please go for a blue/green color scheme. THE DESIGN MUST BE BOLD

Target Market(s)

adults ages 30 - 64

Font styles to use
Sans Serif

Colors
0455a3
cedeed
3176b5
85acd3
cfdeed
9bcb3b
abd037
cadf82
00a990

Requirements
Must have
• - bold design
• - somewhat gender-neutral color scheme because this will be used equally by men and women
• - B12 MUST be very prominent and visible on the label
Should not have
• - it should not be "crunchy" looking

```html
<!DOCTYPE html>
<html lang="en">
<head>
<meta charset="utf-8">
<title>Zulpa Vitamin B12 Drops Label</title>
<link rel="stylesheet" href="https://fonts.googleapis.com/css2?family=Mulish:wght@400;600;700;900&family=Roboto+Slab:wght@900&display=swap">
<style>
  :root {
    --page: #ffffff;
    --label: #e8e9eb;
    --teal: #14a89a;
    --teal-text: #1aa592;
    --purple: #2b1a47;
    --ink: #1b1630;
    --white: #ffffff;
  }
  * { box-sizing: border-box; margin: 0; padding: 0; }
  html, body { width: 1200px; height: 1000px; overflow: hidden; background: var(--page); }
  body { position: relative; font-family: "Mulish", Arial, sans-serif; }

  .label { position: absolute; left: 92px; top: 58px; width: 1024px; height: 462px; background: var(--label); overflow: hidden; }

  .pattern-band { position: absolute; left: 0; top: 258px; width: 714px; height: 204px;
    background: linear-gradient(180deg, #1aae9f 0%, #12a293 100%); }

  /* nutrition panel */
  .nutrition { position: absolute; left: 52px; top: 34px; width: 152px; color: var(--teal-text); }
  .nutrition-title { font-size: 17px; font-weight: 700; padding-left: 0; }
  .nutrition-rule { height: 4px; background: var(--teal); margin: 10px 0 12px; width: 151px; }
  .nutrition-table { border: 3px solid var(--teal); width: 148px; margin-left: -4px; }
  .nutrition-row { font-size: 11px; font-weight: 700; line-height: 12px; padding: 4px 6px 4px 6px; }
  .nutrition-row + .nutrition-row { border-top: 3px solid var(--teal); }
  .nutrition-row.group-a { padding: 5px 6px 3px; }
  .nutrition-row.group-b { padding: 6px 6px 7px; }
  .nutrition-row.group-c { padding: 6px 6px 4px; line-height: 14px; }

  /* front panel */
  .brand-band { position: absolute; left: 368px; top: 0; width: 288px; height: 93px; background: var(--purple);
    border-bottom: 4px solid var(--teal); display: flex; align-items: center; justify-content: center; }
  .brand-name { font-family: "Mulish", Arial, sans-serif; font-weight: 900; font-size: 54px; color: var(--white); letter-spacing: 1px; }
  .drop-icon { position: absolute; left: 539px; top: 102px; width: 60px; height: 76px; }
  .product-band { position: absolute; left: 358px; top: 220px; width: 308px; height: 100px; background: var(--purple);
    display: flex; align-items: center; justify-content: center; gap: 4px; color: var(--white); }
  .product-side { writing-mode: vertical-rl; transform: rotate(180deg); font-size: 15px; font-weight: 700; letter-spacing: 0.5px; }
  .product-side.right { transform: none; font-weight: 900; }
  .product-main { font-family: "Roboto Slab", Georgia, serif; font-weight: 900; font-size: 76px; line-height: 1; color: #f2f0ea; }
  .volume-tag { position: absolute; left: 405px; top: 422px; width: 214px; height: 50px; background: var(--purple); border-radius: 8px;
    color: var(--white); font-size: 13px; text-align: center; padding-top: 12px; }

  /* info panel */
  .info { position: absolute; left: 743px; top: 42px; width: 238px; }
  .info-heading { font-size: 18px; font-weight: 700; color: var(--ink); margin-bottom: 8px; }
  .info-text { font-size: 13px; line-height: 17px; color: var(--teal-text); text-align: justify; margin-bottom: 14px; }
  .maker { position: absolute; left: 743px; top: 306px; font-size: 15px; line-height: 19px; color: var(--ink); }
  .batch-box { position: absolute; left: 870px; top: 359px; width: 110px; height: 47px; border: 2px solid var(--ink);
    font-size: 13px; line-height: 17px; color: var(--ink); padding: 3px 9px; }
</style>
</head>
<body>
  <section class="label">
    <div class="pattern-band" role="img" aria-label="Decorative teal leaf pattern on white"></div>

    <div class="nutrition">
      <h2 class="nutrition-title">Nutrition Facts</h2>
      <div class="nutrition-rule"></div>
      <div class="nutrition-table">
        <div class="nutrition-row group-a">Lorem ipsum<br>Lorem ipsum<br>Lorem ipsum</div>
        <div class="nutrition-row group-b">Lorem ipsum</div>
        <div class="nutrition-row group-c">Lorem ipsum<br>Lorem ipsum<br>Lorem ipsum<br>Lorem ipsum</div>
      </div>
    </div>

    <div class="brand-band"><span class="brand-name">ZULPA</span></div>

    <svg class="drop-icon" viewBox="0 0 60 76" aria-hidden="true">
      <defs>
        <linearGradient id="dropFill" x1="0" y1="0" x2="1" y2="1">
          <stop offset="0" stop-color="#14a89a"/>
          <stop offset="1" stop-color="#3a2360"/>
        </linearGradient>
      </defs>
      <path d="M30 2 C38 22 56 36 56 50 A26 26 0 0 1 4 50 C4 36 22 22 30 2 Z" fill="url(#dropFill)"/>
      <path d="M44 46 C46 56 40 64 32 66" stroke="#ffffff" stroke-width="4" fill="none" stroke-linecap="round"/>
    </svg>

    <div class="product-band">
      <span class="product-side">vitamin</span>
      <span class="product-main">B12</span>
      <span class="product-side right">drops</span>
    </div>

    <div class="volume-tag">2 FL OZ (60ml)</div>

    <div class="info">
      <h3 class="info-heading">Ingredient</h3>
      <p class="info-text">Lorem ipsum dolor sit amet, consectetuer adipiscing elit, sed diam nonummy nibh euismod tincidunt ut laoreet</p>
      <h3 class="info-heading">Recommendation</h3>
      <p class="info-text">Lorem ipsum dolor sit amet, consectetuer adipiscing elit, sed diam nonummy nibh euismod tincidunt ut laoreet</p>
    </div>

    <p class="maker">Company Address<br>Made in Switzerland</p>
    <div class="batch-box">Batch:<br>Expiry Date:</div>
  </section>
</body>
</html>
```